Placing my newer logo on my existing business card

I have a business card that I had you guys do years ago, then I changed my logo, I love both my business card and my logo. The challenge is both my logo and my business card are very similar in color. So I'm not sure how to make my logo stand out.

Sick

```html
<!DOCTYPE html>
<html lang="en">
<head>
<meta charset="utf-8">
<title>Vitality Wellness &amp; Balance Clinic – Business Cards</title>
<link rel="stylesheet" href="https://fonts.googleapis.com/css2?family=Cinzel:wght@500;600&family=Tinos:wght@400;700&family=Quicksand:wght@500&display=swap">
<style>
  :root {
    --bg: #2b2c30;
    --paper: #ffffff;
    --teal: #7fa6ab;
    --rust: #b04a2c;
    --ink: #5e5e5e;
    --rule: #d7dcdd;
  }
  html, body {
    margin: 0;
    width: 1200px;
    height: 952px;
    overflow: hidden;
    background: var(--bg);
  }
  .card {
    position: absolute;
    top: 322px;
    width: 540px;
    height: 308px;
    background: var(--paper);
    overflow: hidden;
    box-shadow: 0 10px 30px rgba(0,0,0,.45);
  }
  .card--front { left: 30px; }
  .card--back { left: 630px; }

  .clinic-name {
    position: absolute;
    margin: 0;
    font-family: "Cinzel", serif;
    font-weight: 600;
    color: var(--rust);
    letter-spacing: .06em;
    line-height: 1.1;
    text-transform: uppercase;
  }
  .card--front .clinic-name { left: 34px; top: 50px; font-size: 17px; }
  .brand-dot {
    position: absolute;
    left: 196px; top: 12px;
    width: 28px; height: 28px;
    border-radius: 50%;
    background: var(--teal);
  }

  .person { position: absolute; left: 262px; top: 104px; }
  .person__name {
    margin: 0;
    font-family: "Tinos", serif;
    font-weight: 700;
    font-size: 28px;
    line-height: 1;
  }
  .person__first { color: var(--teal); }
  .person__last { color: var(--rust); }
  .person__title {
    margin: 4px 0 0;
    font-family: "Tinos", serif;
    font-size: 14px;
    color: var(--ink);
  }
  .person__rule { width: 48px; height: 1px; background: var(--ink); margin-top: 8px; }

  .contacts {
    position: absolute;
    left: 242px; top: 164px;
    margin: 0; padding: 0;
    list-style: none;
    font-family: "Tinos", serif;
    font-size: 12px;
    color: var(--ink);
    line-height: 1.25;
  }
  .contacts li { display: flex; align-items: flex-start; gap: 7px; margin-bottom: 3px; }
  .icon {
    flex: none;
    width: 14px; height: 14px;
    border-radius: 3px;
    background: var(--teal);
    display: flex; align-items: center; justify-content: center;
  }
  .icon--pin { background: var(--rust); }
  .icon svg { width: 10px; height: 10px; fill: #fff; }

  .band { position: absolute; left: 0; top: 278px; width: 540px; height: 12px; }

  .card--back .clinic-name { left: 36px; top: 34px; font-size: 16px; }
  .appointment {
    position: absolute;
    left: 28px; top: 96px;
    font-family: "Quicksand", sans-serif;
    font-size: 11px;
    color: var(--teal);
  }
  .appointment__row { display: flex; align-items: flex-end; gap: 4px; height: 30px; }
  .appointment__line { width: 150px; border-bottom: 1px solid var(--rule); margin-bottom: 2px; }
  .back-art { position: absolute; right: 0; top: 0; }
  .back-art__name {
    font-family: "Cinzel", serif;
    font-weight: 600;
    font-size: 15px;
    fill: #ffffff;
    letter-spacing: .06em;
  }
</style>
</head>
<body>

<section class="card card--front" aria-label="Business card front">
  <span class="brand-dot" aria-hidden="true"></span>
  <h1 class="clinic-name">Vitality Wellness<br>&amp; Balance Clinic</h1>

  <div class="person">
    <p class="person__name"><span class="person__first">Marla</span> <span class="person__last">Jennings</span></p>
    <p class="person__title">Managing Director</p>
    <div class="person__rule"></div>
  </div>

  <ul class="contacts">
    <li><span class="icon icon--pin"><svg viewBox="0 0 10 10"><path d="M5 0a3.5 3.5 0 0 0-3.5 3.5C1.5 6 5 10 5 10s3.5-4 3.5-6.5A3.5 3.5 0 0 0 5 0zm0 5a1.5 1.5 0 1 1 0-3 1.5 1.5 0 0 1 0 3z"/></svg></span><span>1420 Harbor Rd ste#3<br>north Alden Utah 84000</span></li>
    <li><span class="icon"><svg viewBox="0 0 10 10"><path d="M2.2 0.5 3.8 2.4 3 3.6c.6 1.4 1.9 2.8 3.4 3.4l1.2-.8 1.9 1.6-.9 1.6C4.6 9.5.5 5.4.6 1.4z"/></svg></span><span>1(555)010-4821</span></li>
    <li><span class="icon"><svg viewBox="0 0 10 10"><path d="M1 2h8v6H1zM1.6 2.6 5 5.4l3.4-2.8"/></svg></span><span>vitalitywellness@mail.com</span></li>
    <li><span class="icon"><svg viewBox="0 0 10 10"><path d="M5 1 8 9 5 7 2 9z"/></svg></span><span>www.vitalitywellnessclinic.com</span></li>
  </ul>

  <svg class="band" viewBox="0 0 540 12" aria-hidden="true">
    <rect x="0" y="1" width="206" height="2" fill="var(--teal)"/>
    <polygon points="200,0 540,0 540,6 206,6" fill="var(--rust)"/>
  </svg>
</section>

<section class="card card--back" aria-label="Business card back">
  <h2 class="clinic-name">Vitality Wellness<br>&amp; Balance Clinic</h2>

  <div class="appointment">
    <div class="appointment__row"><span>Time :</span><span class="appointment__line"></span></div>
    <div class="appointment__row"><span>Date :</span><span class="appointment__line"></span></div>
  </div>

  <svg class="back-art" width="540" height="308" viewBox="0 0 540 308" aria-hidden="true">
    <path d="M300 308 C330 250 380 235 430 228 C480 220 520 200 540 170 L540 308 Z" fill="var(--rust)"/>
    <circle cx="420" cy="160" r="100" fill="var(--teal)"/>
    <text class="back-art__name" x="420" y="156" text-anchor="middle">Vitality</text>
    <text class="back-art__name" x="420" y="176" text-anchor="middle">Wellness</text>
  </svg>
</section>

</body>
</html>
```